Fitness Body Weight Exercises Book Cover

Need a book cover design for a new book

This book is going to market to people to get in shape by playing a fitness dice game call FlexTRIO The dice game

When people see the cover they should see that this is a book that can help them get in shape. We are positioning the guru as an expert inside of the fitness niche

Target Market(s)

fitness

Requirements
Must have
• The name of the book which is

"The Grand Summit Frame Regimen"

Tagline -

The Worlds #1 Resource For Combat Strength Training Using Body Weight Exercises For Men, Women and Children

__________

Featuring FlexTRIO The Dice Game (TM)

___________________________
ON THE BACK COVER

Image with Oren with his gold medal
with these words
No Weights, No Problem

_____-

front cover
the image with him doing a push up should be on the front of the cover with these words

_________
Nice to have
• Maybe

"Oren Presents ...."

The Grand Summit Frame Regimen

```html
<!DOCTYPE html>
<html lang="en">
<head>
<meta charset="utf-8">
<title>The Grand Summit Frame Regimen – Book Cover</title>
<link rel="stylesheet" href="https://fonts.googleapis.com/css2?family=Anton&family=Oswald:wght@700&family=Quicksand:wght@600;700&display=swap">
<style>
  :root {
    --stage: #04132b;
    --navy: #1c1f3f;
    --navy-deep: #10132c;
    --gold: #f5b62a;
    --gold-bright: #fcc419;
    --gold-deep: #e8a21c;
    --red: #b8131b;
    --band-red: #c8232c;
    --ink: #0d0d0d;
    --white: #ffffff;
  }
  * { margin: 0; padding: 0; box-sizing: border-box; }
  html, body { width: 1200px; height: 1200px; overflow: hidden; }
  body {
    background: var(--stage);
    position: relative;
    font-family: "Quicksand", sans-serif;
  }
  .cover {
    position: absolute;
    top: 200px;
    width: 520px;
    height: 790px;
    overflow: hidden;
  }

  /* Back cover */
  .back-cover {
    left: 60px;
    background: linear-gradient(180deg, var(--navy) 0%, var(--navy-deep) 62%, var(--gold) 62%, var(--gold-bright) 100%);
  }
  .back-cover .bands { position: absolute; inset: 0; }
  .back-cover .medal-photo {
    position: absolute;
    left: 230px;
    top: 110px;
    width: 290px;
    height: 470px;
    border-radius: 120px 0 0 0;
    background: linear-gradient(160deg, #5a3a28 0%, #a2704f 45%, #6b4632 100%);
  }
  .back-cover .slogan {
    position: absolute;
    left: 55px;
    top: 430px;
    transform: rotate(-90deg);
    transform-origin: left top;
    font-family: "Oswald", sans-serif;
    font-weight: 700;
    font-size: 58px;
    line-height: 1.05;
    text-transform: uppercase;
    white-space: nowrap;
  }
  .slogan .line-white { color: var(--white); display: block; }
  .slogan .line-gold { color: var(--gold-bright); display: block; }
  .back-cover .imprint {
    position: absolute;
    left: 60px;
    bottom: 70px;
    color: var(--navy-deep);
  }
  .imprint .featuring { font-size: 20px; font-weight: 700; line-height: 1.2; }
  .imprint .meta { font-size: 16px; font-weight: 700; margin-top: 10px; line-height: 1.5; }

  /* Front cover */
  .front-cover {
    left: 620px;
    background:
      radial-gradient(circle at 70% 40%, var(--gold-bright) 0%, var(--gold) 55%, var(--gold-deep) 100%);
  }
  .front-cover .splash {
    position: absolute;
    left: 0;
    top: 0;
    width: 260px;
    height: 150px;
    background: var(--ink);
    clip-path: polygon(0 0, 100% 0, 82% 30%, 40% 48%, 18% 100%, 0 90%);
  }
  .front-cover .presents {
    position: absolute;
    left: 100px;
    top: 70px;
    background: var(--band-red);
    color: var(--white);
    font-family: "Oswald", sans-serif;
    font-weight: 700;
    font-size: 28px;
    letter-spacing: 14px;
    padding: 2px 8px 2px 16px;
    text-transform: uppercase;
  }
  .front-cover .title {
    position: absolute;
    left: 100px;
    top: 116px;
    width: 410px;
    font-family: "Anton", sans-serif;
    font-size: 86px;
    line-height: 0.96;
    text-transform: uppercase;
  }
  .title span { display: block; }
  .title .ink { color: var(--ink); }
  .title .red { color: var(--red); }
  .front-cover .tagline {
    position: absolute;
    left: 100px;
    top: 462px;
    width: 390px;
    font-size: 19px;
    font-weight: 700;
    line-height: 1.22;
    color: var(--ink);
  }
  .front-cover .pushup-photo {
    position: absolute;
    left: 0;
    bottom: 0;
    width: 520px;
    height: 300px;
    background: linear-gradient(180deg, rgba(245,182,42,0) 0%, rgba(245,182,42,0) 15%, #9a7420 50%, #6e5216 100%);
  }
  .front-cover .featuring {
    position: absolute;
    left: 0;
    right: 0;
    bottom: 40px;
    text-align: center;
    color: var(--white);
    font-size: 20px;
    font-weight: 700;
    line-height: 1.2;
    text-transform: uppercase;
  }
</style>
</head>
<body>
  <section class="cover back-cover">
    <svg class="bands" viewBox="0 0 520 790" aria-hidden="true">
      <polygon points="300,0 520,0 520,60" fill="var(--gold)"/>
      <line x1="120" y1="60" x2="520" y2="250" stroke="#2c3060" stroke-width="2"/>
      <polygon points="0,470 520,560 520,600 0,520" fill="var(--gold)" opacity="0.85"/>
      <polygon points="60,560 330,600 330,620 60,585" fill="var(--gold-bright)"/>
      <polygon points="0,600 520,690 520,790 0,790" fill="var(--gold-bright)"/>
    </svg>
    <div class="medal-photo" role="img" aria-label="Photo of Oren smiling, wearing a cap and his gold medal"></div>
    <h2 class="slogan">
      <span class="line-white">No Weights,</span>
      <span class="line-gold">No Problem</span>
    </h2>
    <div class="imprint">
      <p class="featuring">FEATURING<br>FlexTRIO The Dice Game™</p>
      <p class="meta">Published By:<br>Date:</p>
    </div>
  </section>

  <section class="cover front-cover">
    <div class="splash" aria-hidden="true"></div>
    <p class="presents">Oren Presents</p>
    <h1 class="title">
      <span class="ink">The Grand</span>
      <span class="red">Summit</span>
      <span class="ink">Frame</span>
      <span class="red">Regimen</span>
    </h1>
    <p class="tagline">The Worlds #1 Resource For Combat Strength Training Using Body Weight Exercises For Men, Women and Children.</p>
    <div class="pushup-photo" role="img" aria-label="Photo of Oren doing a push-up, toned in gold"></div>
    <p class="featuring">Featuring FlexTRIO<br>The Dice Game (TM)</p>
  </section>
</body>
</html>
```